Risk Management Company in need of Business Card Design

We sell risk management insurance to Lenders (Banks, Credit Unions, Real Estate Trust).

We need a very clean, professional card that will leave a great impression.

We are looking to use a blue color for our logo on the card (Preferably close to royal blue but are open to looking at navy blue or any darker blues as well).

Please see the logo attached to get an idea. We are open to writing Harbor Shield Under the logo or next to the logo. Really whatever looks best.

Target Market(s)

Banks, Credit Unions, Real Estate Trusts

Industry/Entity Type

Insurance

Contact Information for Business Card

Name: Mark Dunstan
Title: Regional Sales Director
Email: mdunstan@harborshield.example
C:617-555-0143
D:617-555-0187
800-555-0129 Ext.318
F:781-555-0164 (We would like to see some cards without the fax number as well to compare)

Company Name: Harbor Shield
Website: www.harborshield.example

Address: 118 E. Morrow St. Suite 420, Calder Point, MD 21299 (Preferably written on the bottom of the card in small print.)

Colors
0355a3
0455a3

Requirements
Nice to have
• We would like to see a couple of where the back has the logo in reverse colors (Logo White, Background Blue)

```html
<!DOCTYPE html>
<html lang="en">
<head>
<meta charset="utf-8">
<title>Harbor Shield – Business Cards</title>
<link rel="stylesheet" href="https://fonts.googleapis.com/css2?family=Oswald:wght@600&family=Tinos:wght@400&display=swap">
<style>
  :root {
    --navy: #0c1957;
    --accent-blue: #1d5db0;
    --ink: #151515;
    --white: #ffffff;
    --board-light: #5c5c5c;
    --board-dark: #0b0b0b;
  }
  html, body {
    margin: 0;
    padding: 0;
    width: 1200px;
    height: 1000px;
    overflow: hidden;
  }
  .board {
    position: relative;
    width: 1200px;
    height: 1000px;
    background: radial-gradient(ellipse 70% 65% at 50% 40%, var(--board-light) 0%, #2c2c2c 60%, var(--board-dark) 100%);
    font-family: "Tinos", "Times New Roman", serif;
  }
  .label {
    position: absolute;
    font-family: "Oswald", "Arial Narrow", sans-serif;
    font-weight: 600;
    font-size: 29px;
    letter-spacing: 2px;
    color: var(--white);
    text-transform: uppercase;
    transform: translateX(-50%);
    white-space: nowrap;
    line-height: 1;
  }
  .card {
    position: absolute;
    width: 580px;
    height: 331px;
    overflow: hidden;
  }
  .card--back { background: var(--navy); }
  .card--front { background: var(--white); }
  .band {
    position: absolute;
    left: 0;
    width: 100%;
    background: var(--navy);
  }
  .band--top { top: 0; height: 12px; }
  .band--bottom { bottom: 0; height: 12px; }
  .stripe { position: absolute; }
  .wordmark {
    position: absolute;
    transform: translateX(-50%);
    white-space: nowrap;
    text-transform: uppercase;
    letter-spacing: 1px;
    font-size: 30px;
    line-height: 1;
  }
  .card--back .wordmark { color: var(--white); }
  .card--front .wordmark { color: var(--navy); }
  .website {
    position: absolute;
    left: 360px;
    top: 286px;
    font-size: 17px;
    color: var(--white);
  }
  .person { position: absolute; }
  .person__name {
    font-size: 27px;
    color: var(--ink);
    text-transform: uppercase;
    line-height: 1;
    margin: 0;
    font-weight: 400;
  }
  .person__title {
    font-size: 13.5px;
    color: var(--accent-blue);
    margin-top: 0;
  }
  .contacts {
    position: absolute;
    list-style: none;
    margin: 0;
    padding: 0;
    font-size: 13.5px;
    color: var(--ink);
  }
  .contacts li {
    display: flex;
    align-items: flex-start;
    line-height: 16px;
    margin-bottom: 3px;
    white-space: nowrap;
  }
  .contacts svg {
    flex: none;
    width: 12px;
    height: 12px;
    margin: 2px 8px 0 0;
    fill: var(--accent-blue);
  }
</style>
</head>
<body>
<svg width="0" height="0" style="position:absolute" aria-hidden="true">
  <symbol id="icon-phone" viewBox="0 0 12 12"><path d="M1 4.5C1 3 3 2 6 2s5 1 5 2.5V5H8.5V4H3.5v1H1z"/><rect x="2" y="6" width="8" height="5" rx="1"/></symbol>
  <symbol id="icon-mail" viewBox="0 0 12 12"><rect x="0.5" y="3" width="11" height="6.5"/><path d="M1 3.4 6 7.2 11 3.4" fill="none" stroke="#fff" stroke-width="1"/></symbol>
  <symbol id="icon-mobile" viewBox="0 0 12 12"><rect x="3" y="0.5" width="6" height="11" rx="1"/><rect x="4" y="1.8" width="4" height="7.5" fill="#fff"/></symbol>
  <symbol id="icon-fax" viewBox="0 0 12 12"><rect x="3" y="1" width="6" height="3.5"/><rect x="1" y="5" width="10" height="5.5" rx="1"/><rect x="3.5" y="7" width="5" height="1.2" fill="#fff"/></symbol>
  <symbol id="icon-home" viewBox="0 0 12 12"><path d="M6 0.8 0.5 6h1.5v5.2h3V8h2v3.2h3V6h1.5z"/></symbol>
</svg>

<main class="board">
  <div class="label" style="left:273px; top:131px;">Back Card</div>
  <div class="label" style="left:900px; top:131px;">Front Card without Fax Number</div>

  <section class="card card--back" style="left:10px; top:174px;">
    <svg class="stripe" style="left:0; top:0;" width="580" height="331">
      <polygon points="276,26 580,26 580,40 272,40" fill="#fff"/>
      <polygon points="0,289 308,289 303,302 0,302" fill="#fff"/>
    </svg>
    <div class="wordmark" style="left:162px; top:209px;">Harbor Shield</div>
    <div class="website">www.harborshield.example</div>
  </section>

  <section class="card card--front" style="left:610px; top:174px;">
    <div class="band band--top"></div>
    <div class="band band--bottom"></div>
    <div class="wordmark" style="left:141px; top:213px;">Harbor Shield</div>
    <div class="person" style="left:307px; top:90px;">
      <h2 class="person__name">Mark Dunstan</h2>
      <div class="person__title">Regional Sales Director</div>
    </div>
    <ul class="contacts" style="left:308px; top:159px;">
      <li><svg><use href="#icon-phone"/></svg>617-555-0187/800-555-0129 Ext.318</li>
      <li><svg><use href="#icon-mail"/></svg>mdunstan@harborshield.example</li>
      <li><svg><use href="#icon-mobile"/></svg>617-555-0143</li>
      <li><svg><use href="#icon-home"/></svg><span>118 E. Morrow St. Suite 420,<br>Calder Point, MD 21299</span></li>
    </ul>
  </section>

  <section class="card card--front" style="left:320px; top:534px;">
    <div class="band band--top"></div>
    <div class="band band--bottom"></div>
    <div class="wordmark" style="left:142px; top:205px;">Harbor Shield</div>
    <div class="person" style="left:306px; top:91px;">
      <h2 class="person__name">Mark Dunstan</h2>
      <div class="person__title">Regional Sales Director</div>
    </div>
    <ul class="contacts" style="left:306px; top:157px;">
      <li><svg><use href="#icon-phone"/></svg>617-555-0187/800-555-0129 Ext.318</li>
      <li><svg><use href="#icon-mail"/></svg>mdunstan@harborshield.example</li>
      <li><svg><use href="#icon-mobile"/></svg>617-555-0143</li>
      <li><svg><use href="#icon-fax"/></svg>781-555-0164</li>
      <li><svg><use href="#icon-home"/></svg><span>118 E. Morrow St. Suite 420,<br>Calder Point, MD 21299</span></li>
    </ul>
  </section>

  <div class="label" style="left:610px; top:880px;">Front Card with Fax Number</div>
</main>
</body>
</html>
```